Powepoint template for an investment group

Need high end clear clean concise creative luxurious

Have royal clients
High end/billionaire investors

Using ross gold logo can be creative
Must habe page numbers
Logo preference header top right
Page number footer bottom right

The first page of the ppt maybe a big block of dark grey and oberi investment group written on the front page in rose gold

Target Market(s)

Investors at a high level

Requirements
Must have
• Luxury feel

```html
<!DOCTYPE html>
<html lang="en">
<head>
<meta charset="utf-8">
<title>Oberi Investment Group – Presentation</title>
<link href="https://fonts.googleapis.com/css2?family=Jost:wght@300;400;500&family=Arimo:wght@400&display=swap" rel="stylesheet">
<style>
:root{
  --sheet:#dddddd;
  --charcoal:#262424;
  --rose-gold:#f1b8ab;
  --footer-pink:#f2bab3;
  --heading-rose:#a9665c;
  --circle-rose:#9b5a53;
  --icon-rose:#a8635a;
  --bronze:#b57a45;
  --ink:#1c1c1c;
  --body-text:#333333;
  --card-line:#8d8d8d;
  --pale:#eef2f5;
  --texture-grey:#d4d4d4;
}
*{box-sizing:border-box;margin:0;padding:0}
html,body{width:1200px;height:4231px;overflow:hidden;background:var(--sheet)}
body{position:relative;font-family:"Jost",sans-serif;color:var(--ink)}
.slide{position:absolute;left:36px;width:1130px;height:633px;background:#fff;overflow:hidden;box-shadow:0 2px 6px rgba(0,0,0,.25)}
.slide-footer{position:absolute;left:0;bottom:0;width:100%;height:42px;background:var(--footer-pink);font:400 13px "Jost",sans-serif;color:#2a2a2a;display:flex;align-items:center;justify-content:center}
.page-number{position:absolute;right:22px;top:13px;font-size:12px}
.abs{position:absolute}
.photo{position:absolute}
.body-copy{font-family:"Arimo",sans-serif;color:var(--body-text)}

/* cover */
.cover-bg{left:0;top:0;width:1130px;height:591px;background:radial-gradient(ellipse at 50% 40%,#34302e 0%,#262323 60%,#1d1b1b 100%)}
.cover-frame{left:222px;top:169px;width:666px;height:294px;border:1px solid #77706d}
.cover-title{left:222px;top:176px;width:666px;text-align:center;font:400 72px/94px "Jost",sans-serif;color:var(--rose-gold);letter-spacing:1px}
.rule{position:absolute;width:1px;background:#8a8380}
.dot{position:absolute;width:9px;height:9px;border-radius:50%}
.brand-name{position:absolute;right:30px;top:26px;font:400 14px "Jost",sans-serif;color:var(--rose-gold)}

/* about */
.about-title{left:330px;top:124px;width:470px;text-align:center;font:400 46px "Jost",sans-serif;color:var(--heading-rose)}
.about-text{left:355px;top:196px;width:417px;text-align:center;font-size:11.8px;line-height:26px}
.about-text p+p{margin-top:16px}

/* advisory */
.texture-block{left:36px;top:30px;width:188px;height:84px;background:var(--texture-grey)}
.advisory-title{left:33px;top:155px;font:400 39px/51px "Jost",sans-serif;color:var(--ink);letter-spacing:1.5px}
.advisory-text{left:31px;top:283px;width:500px;font-size:14.3px;line-height:29px}
.bronze-bar{position:absolute;top:0;width:4px;background:var(--bronze)}

/* benefits */
.benefit-bg{left:0;top:0;width:1130px;height:591px;background:linear-gradient(100deg,#0d1426 0%,#1c2a45 35%,#131d33 65%,#0e1628 100%)}
.benefit-circle{left:601px;top:69px;width:492px;height:447px;border-radius:50%;background:var(--circle-rose)}
.benefit-title{left:630px;top:166px;width:434px;text-align:center;font:400 31px/45px "Jost",sans-serif;color:#fff}
.benefit-text{left:650px;top:267px;width:394px;text-align:center;font-size:12.6px;line-height:27px;color:#f4e6e3}

/* why */
.why-bg{left:0;top:0;width:1130px;height:591px;background:linear-gradient(180deg,#f4f6f8 0%,var(--pale) 100%)}
.why-title{left:0;top:48px;width:1130px;text-align:center;font:400 42px "Jost",sans-serif;color:var(--ink)}
.why-card{position:absolute;top:135px;width:295px;height:387px;border:1px solid var(--card-line);border-radius:22px;text-align:center}
.why-icon{position:absolute;left:108px;top:28px}
.why-card h3{position:absolute;left:0;top:138px;width:100%;font:500 19px "Jost",sans-serif;color:var(--ink)}
.why-card p{position:absolute;left:16px;top:182px;width:261px;font-size:13px;line-height:27px}

/* thanks */
.thanks-panel{left:0;top:0;width:144px;height:591px;background:#fff}
.thanks-word{position:absolute;left:10px;top:118px;width:104px;height:400px;writing-mode:vertical-rl;font:500 78px/104px "Jost",sans-serif;color:#111;text-align:center}
.thanks-photo{left:144px;top:0;width:986px;height:591px;background:linear-gradient(180deg,#3c5d8d 0%,#6c88b0 40%,#3b4c66 75%,#2a3347 100%)}
</style>
</head>
<body>

<!-- Slide 1: Cover -->
<section class="slide" style="top:66px">
  <div class="photo cover-bg" role="img" aria-label="Darkened photo of a business meeting around a table"></div>
  <div class="rule" style="left:62px;top:0;height:97px"></div>
  <div class="dot" style="left:58px;top:93px;background:var(--rose-gold)"></div>
  <div class="rule" style="left:80px;top:0;height:327px"></div>
  <div class="dot" style="left:76px;top:323px;background:#fff"></div>
  <div class="rule" style="left:1079px;top:305px;height:286px"></div>
  <div class="dot" style="left:1075px;top:301px;background:var(--rose-gold)"></div>
  <div class="rule" style="left:1060px;top:535px;height:56px"></div>
  <div class="dot" style="left:1056px;top:531px;background:#fff"></div>
  <div class="brand-name">Oberi Investment Group</div>
  <div class="abs cover-frame"></div>
  <h1 class="abs cover-title">Oberi Investment<br>Group</h1>
  <footer class="slide-footer">© 2022 All Rights Reserved<span class="page-number">1</span></footer>
</section>

<!-- Slide 2: About -->
<section class="slide" style="top:759px">
  <div class="photo" style="left:31px;top:61px;width:283px;height:445px;background:linear-gradient(160deg,#8b8f93 0%,#6c5e55 50%,#3b3a3c 100%)" role="img" aria-label="Photo of three colleagues discussing work at a desk"></div>
  <h2 class="abs about-title">About Us</h2>
  <div class="abs about-text body-copy">
    <p>Lorem ipsum dolor sit amet, consectetur adipiscing elit, sed do eiusmod tempor incididunt ut labore et dolore magna aliqua. Ut enim ad veniam, quis nostrud exercitation ullamco laboris nisi ut aliquip ex consequat. Duis aute irure dolor in reprehenderit in voluptate velit esse cillum dolore eu fugiat nulla pariatur. Excepteur sint occaecat cupidatat non proident, sunt in culpa qui officia deserunt laborum.</p>
    <p>Lorem ipsum dolor sit amet, consectetur adipiscing elit, sed do eiusmod tempor incididunt ut labore et dolore magna aliqua. Ut enim ad veniam, quis nostrud exercitation ullamco laboris nisi ut aliquip</p>
  </div>
  <div class="photo" style="left:804px;top:61px;width:283px;height:445px;background:linear-gradient(180deg,#e9ebee 0%,#b9bcc0 50%,#6f6a66 100%)" role="img" aria-label="Photo of a presenter speaking to a team in a bright office"></div>
  <footer class="slide-footer">© 2022 All Rights Reserved<span class="page-number">2</span></footer>
</section>

<!-- Slide 3: Advisory -->
<section class="slide" style="top:1452px">
  <div class="abs texture-block" role="img" aria-label="Decorative dotted texture block"></div>
  <h2 class="abs advisory-title">Investment advisory<br>offering to your needs</h2>
  <p class="abs advisory-text body-copy">Lorem ipsum dolor sit amet, consectetur adipiscing elit, sed do eiusmod tempor incididunt ut labore et dolore magna aliqua. Ut enim ad minim veniam, quis nostrud exercitation ullamco laboris nisi ut aliquip ex ea commodo consequat. Duis aute irure dolor in reprehenderit in voluptate velit esse cillum dolore eu fugiat nulla pariatur. Excepteur sint occaecat cupidatat non proident, sunt in culpa qui officia deserunt mollit anim id est laborum</p>
  <div class="photo" style="left:606px;top:0;width:410px;height:558px;border-radius:0 0 100px 100px;background:linear-gradient(150deg,#d9dde2 0%,#6f86a8 40%,#2c3f60 75%,#141b2c 100%)" role="img" aria-label="Photo of two business partners reviewing a tablet"></div>
  <div class="bronze-bar" style="left:1085px;height:294px"></div>
  <div class="bronze-bar" style="left:1096px;height:215px"></div>
  <footer class="slide-footer">© 2022 All Rights Reserved<span class="page-number">3</span></footer>
</section>

<!-- Slide 4: Benefits -->
<section class="slide" style="top:2145px">
  <div class="photo benefit-bg" role="img" aria-label="Dim photo of a businessman in front of a glowing market chart"></div>
  <div class="abs benefit-circle"></div>
  <h2 class="abs benefit-title">Lets start to discover our<br>Benefits &amp; Features</h2>
  <p class="abs benefit-text body-copy">Lorem ipsum dolor sit amet, consectetur adipiscing elit, sed do eiusmod tempor incididunt ut labore et dolore magna aliqua. Ut enim ad minim veniam, quis nostrud exercitation ullamco laboris nisi ut aliquip ex ea commodo consequat. Duis aute irure dolor in reprehenderit in voluptate velit esse cillum dolore eu fugiat nulla pariatur. Excepteur sint occaecat cupidatat non proident, sunt in culpa qui officia deserunt mollit anim</p>
  <footer class="slide-footer">© 2022 All Rights Reserved<span class="page-number">4</span></footer>
</section>

<!-- Slide 5: Why choose us -->
<section class="slide" style="top:2838px">
  <div class="abs why-bg"></div>
  <h2 class="abs why-title">Why Choose Us</h2>

  <article class="why-card" style="left:92px">
    <svg class="why-icon" width="80" height="80" viewBox="0 0 80 80" fill="none" stroke="var(--icon-rose)" stroke-width="2.4" aria-hidden="true">
      <rect x="4" y="14" width="52" height="40" rx="2"/>
      <path d="M4 46h52M22 54v10M38 54v10M16 64h30"/>
      <path d="M14 40v-8M22 40v-14M30 40v-10"/>
      <path d="M42 34V10M50 30V4M58 34V14"/>
      <circle cx="58" cy="56" r="10"/><path d="M65 63l10 10"/>
    </svg>
    <h3>We Deal With Love</h3>
    <p class="body-copy">Lorem ipsum dolor sit amet, adipiscing elit, sed do eiusmod tempor incididunt dolore magna aliqua. veniam, quis nostrud ullamco laboris nisi ut aliquip ex consequat. Duis aute irure reprehenderit in voluptate cillum dolore eu fugiat nulla pariatur.occaecat</p>
  </article>

  <article class="why-card" style="left:417px">
    <svg class="why-icon" width="80" height="80" viewBox="0 0 80 80" fill="none" stroke="var(--icon-rose)" stroke-width="2.4" aria-hidden="true">
      <rect x="4" y="6" width="40" height="54" rx="2"/>
      <path d="M12 18h22M12 26h22M12 34h14"/>
      <circle cx="62" cy="20" r="7"/><path d="M62 8v5M62 27v5M50 20h5M69 20h5"/>
      <rect x="22" y="42" width="52" height="32" rx="3"/>
      <path d="M40 42v-6h16v6M22 56h52M46 52h4v8h-4z"/>
    </svg>
    <h3>We Are Professionals</h3>
    <p class="body-copy">Lorem ipsum dolor sit amet, adipiscing elit, sed do eiusmod tempor incididunt dolore magna aliqua. veniam, quis nostrud ullamco laboris nisi ut aliquip ex consequat. Duis aute irure reprehenderit in voluptate cillum dolore eu fugiat nulla pariatur.occaecat</p>
  </article>

  <article class="why-card" style="left:740px">
    <svg class="why-icon" width="80" height="80" viewBox="0 0 80 80" fill="none" stroke="var(--icon-rose)" stroke-width="2.4" stroke-linejoin="round" aria-hidden="true">
      <path d="M2 26l12-6 12 24-12 6z"/>
      <path d="M78 26l-12-6-12 24 12 6z"/>
      <path d="M24 40l12 12c3 3 7-1 4-4M32 52l6 6c3 3 7-1 4-4M38 58l4 4c3 3 7-1 4-4l-16-16"/>
      <path d="M56 42L46 52M20 24h10l10-4 14 2"/>
      <path d="M40 20l-8 10c-2 3 2 6 5 4l8-6 11 12"/>
    </svg>
    <h3>We Deliver Our Best</h3>
    <p class="body-copy">Lorem ipsum dolor sit amet, adipiscing elit, sed do eiusmod tempor incididunt dolore magna aliqua. veniam, quis nostrud ullamco laboris nisi ut aliquip ex consequat. Duis aute irure reprehenderit in voluptate cillum dolore eu fugiat nulla pariatur.occaecat</p>
  </article>

  <footer class="slide-footer">© 2022 All Rights Reserved<span class="page-number">5</span></footer>
</section>

<!-- Slide 6: Thank you -->
<section class="slide" style="top:3531px">
  <div class="abs thanks-panel"><span class="thanks-word">Thank You</span></div>
  <div class="photo thanks-photo" role="img" aria-label="Photo of a team working at a long table in a glass-walled office"></div>
  <footer class="slide-footer">© 2022 All Rights Reserved<span class="page-number">6</span></footer>
</section>

</body>
</html>
```